Email Signature

brightLoop Technology is in need of updating our email signature block. We are a technology firm that specializes in cloud services and infrastructure. We would like something that includes, name, title, office addresses (We currently have 3 locations), phone, cell, email and website. We are open to having a logo and motto and looking for something that we can roll out with the new year that is very eye catching.

Industry/Entity Type

Office

Font styles to use
Sans Serif

Requirements
Must have
• Employee name, title, office addresses (We currently have 3 locations), phone, cell, email and website

```html
<!DOCTYPE html>
<html lang="en">
<head>
<meta charset="utf-8">
<title>brightLoop Technology – Email Signature</title>
<link href="https://fonts.googleapis.com/css2?family=Allura&family=Roboto:wght@400;500;700&display=swap" rel="stylesheet">
<style>
  :root {
    --ink: #111111;
    --muted: #7a7a7a;
    --frame: #c9c9c9;
    --divider: #dcdcdc;
    --cell: #f7f7f7;
    --green: #7dbb42;
    --blue: #1e91cf;
    --yellow: #f6c918;
    --orange: #f07122;
    --mark: #9a9a9a;
    --paper: #ffffff;
  }
  html, body {
    margin: 0;
    padding: 0;
    width: 1200px;
    height: 403px;
    overflow: hidden;
    background: var(--paper);
    font-family: "Roboto", Arial, sans-serif;
    color: var(--ink);
  }
  .canvas {
    position: relative;
    width: 1200px;
    height: 403px;
  }
  .signature-card {
    position: absolute;
    left: 80px;
    top: 75px;
    width: 1049px;
    height: 255px;
    border: 1px solid var(--frame);
    box-sizing: border-box;
  }
  .handwritten-name {
    position: absolute;
    left: 140px;
    top: 96px;
    font-family: "Allura", cursive;
    font-size: 50px;
    line-height: 1;
    color: var(--ink);
    white-space: nowrap;
  }
  .brand {
    position: absolute;
    left: 140px;
    top: 190px;
    display: flex;
    align-items: center;
    gap: 12px;
  }
  .brand-square {
    width: 50px;
    height: 50px;
    background: var(--mark);
    border-radius: 6px;
  }
  .brand-name {
    font-size: 20px;
    font-weight: 400;
    color: var(--orange);
    white-space: nowrap;
  }
  .column-divider {
    position: absolute;
    left: 436px;
    top: 100px;
    width: 1px;
    height: 158px;
    background: var(--divider);
  }
  .person-title {
    position: absolute;
    left: 464px;
    top: 101px;
    font-size: 21.5px;
    white-space: nowrap;
  }
  .person-title strong { font-weight: 500; }
  .person-subtitle {
    position: absolute;
    left: 464px;
    width: 640px;
    top: 130px;
    text-align: center;
    font-size: 15px;
    color: var(--ink);
  }
  .office-list {
    position: absolute;
    left: 464px;
    top: 191px;
    margin: 0;
    padding: 0;
    list-style: none;
    font-size: 15.5px;
    line-height: 21.5px;
    white-space: nowrap;
  }
  .office-list b { font-weight: 700; }
  .color-band {
    position: absolute;
    left: 98px;
    top: 274px;
    width: 1012px;
    height: 8px;
    display: flex;
  }
  .color-band span { flex: 1; }
  .band-green { background: var(--green); }
  .band-blue { background: var(--blue); }
  .band-yellow { background: var(--yellow); }
  .band-orange { background: var(--orange); }
  .social-links {
    position: absolute;
    left: 98px;
    top: 285px;
    width: 252px;
    height: 44px;
    background: linear-gradient(90deg, var(--cell), var(--paper));
    display: flex;
  }
  .social-cell {
    display: flex;
    align-items: center;
    justify-content: center;
    border-right: 1px solid var(--divider);
  }
  .social-cell:nth-child(1) { width: 77px; justify-content: flex-end; padding-right: 14px; box-sizing: border-box; }
  .social-cell:nth-child(2) { width: 47px; }
  .social-cell:nth-child(3) { width: 47px; border-right: none; }
  .social-dot {
    width: 14px;
    height: 14px;
    border-radius: 50%;
    background: var(--muted);
  }
  .contact-line {
    position: absolute;
    right: 90px;
    top: 298px;
    font-size: 16px;
    font-weight: 700;
    color: var(--muted);
    white-space: nowrap;
  }
  .contact-line .website { color: var(--orange); }
  .contact-line .sep { font-weight: 400; margin: 0 5px; color: var(--ink); }
</style>
</head>
<body>
<div class="canvas">
  <div class="signature-card"></div>

  <div class="handwritten-name">Dana Kellerby</div>

  <div class="brand">
    <div class="brand-square"></div>
    <div class="brand-name">brightLoop Technology</div>
  </div>

  <div class="column-divider"></div>

  <div class="person-title"><strong>Dana Kellerby</strong> - Client Advocate &amp; Executive Assistant to:</div>
  <div class="person-subtitle">Marco Venn, Co-Founder - Managing Director</div>

  <ul class="office-list">
    <li><b>Corporate Office:</b> 4820 E. Canyon Ridge Drive, Suite 210 | Mesa, AZ 85205</li>
    <li><b>Network Operating Center:</b> 309 N. 52nd St, Suite 1140 | Tempe, AZ 85281</li>
    <li><b>Dallas Office:</b> 1250 Lakeview Park Boulevard, Suite 400 | Dallas, Texas, 75201</li>
  </ul>

  <div class="color-band">
    <span class="band-green"></span>
    <span class="band-blue"></span>
    <span class="band-yellow"></span>
    <span class="band-orange"></span>
  </div>

  <div class="social-links">
    <div class="social-cell"><span class="social-dot" role="img" aria-label="Social profile link"></span></div>
    <div class="social-cell"><span class="social-dot" role="img" aria-label="Social profile link"></span></div>
    <div class="social-cell"><span class="social-dot" role="img" aria-label="Social profile link"></span></div>
  </div>

  <div class="contact-line">
    O: (480) 555-0142<span class="sep">|</span>C: (480) 555-0187<span class="sep">|</span>E: dana@brightloopcorp.com<span class="sep">|</span><span class="website">www.brightloopcorp.com</span>
  </div>
</div>
</body>
</html>
```